Quarlwick Builders Business Cards

I want to use the logo and make an unique business card that shows the textured Logo with brick and builings. I want to be able to stand out when I pass out business cards.

```html
<!DOCTYPE html>
<html lang="en">
<head>
<meta charset="utf-8">
<title>Quarlwick Builders Business Cards</title>
<link rel="stylesheet" href="https://fonts.googleapis.com/css2?family=Roboto:wght@400;500&display=swap">
<style>
  :root {
    --page-bg: #e4e4e4;
    --card-bg: #ffffff;
    --brick-red: #9b2a1f;
    --navy: #111b2e;
    --ink: #1d1d1f;
    --grid-line: #bdbdbd;
    --concrete-light: #85877f;
    --concrete-mid: #5b5d59;
    --concrete-dark: #2c2e2c;
    --tile-text: #f2f2f2;
  }
  * { box-sizing: border-box; margin: 0; padding: 0; }
  html, body { width: 1200px; height: 1200px; overflow: hidden; }
  body {
    background: var(--page-bg);
    font-family: "Roboto", Arial, sans-serif;
    color: var(--ink);
    position: relative;
  }
  .card {
    position: absolute;
    left: 148px;
    width: 904px;
    background: var(--card-bg);
    overflow: hidden;
  }
  .card--front { top: 55px; height: 517px; }
  .card--back { top: 622px; height: 518px; }

  .holder-name {
    position: absolute; left: 52px; top: 82px;
    font-size: 43px; font-weight: 500; letter-spacing: 0.5px;
    color: var(--brick-red); line-height: 1;
  }
  .holder-role {
    position: absolute; left: 52px; top: 134px;
    font-size: 28px; font-weight: 400; line-height: 1;
  }
  .contact-rail {
    position: absolute; left: 53px; top: 259px;
    width: 44px; bottom: 0;
    background: var(--navy);
  }
  .contact-rail__cap {
    position: absolute; left: 0; top: 0; width: 100%; height: 24px;
    background: var(--brick-red);
  }
  .contact-list { list-style: none; }
  .contact-item {
    position: absolute; left: 0; height: 30px;
    display: flex; align-items: center;
  }
  .contact-item__icon {
    position: absolute; left: 63px; width: 24px; height: 24px;
    display: flex; align-items: center; justify-content: center;
  }
  .contact-item__icon svg { width: 20px; height: 20px; fill: #ffffff; }
  .contact-item__text {
    position: absolute; left: 114px; white-space: nowrap;
    font-size: 26px; line-height: 30px;
  }
  .contact-item--phone { top: 301px; }
  .contact-item--mail { top: 344px; }
  .contact-item--web { top: 386px; }
  .contact-item--place { top: 429px; }

  .brand-tile {
    position: absolute;
    background: radial-gradient(ellipse at 50% 45%, var(--concrete-light) 0%, var(--concrete-mid) 55%, var(--concrete-dark) 100%);
    display: flex; align-items: center; justify-content: center;
    text-align: center;
  }
  .brand-tile__name {
    font-family: "Roboto", Arial, sans-serif;
    font-weight: 500; color: var(--tile-text);
    line-height: 1; white-space: nowrap;
  }
  .card--front .brand-tile { left: 541px; top: 0; width: 301px; height: 324px; }
  .card--front .brand-tile__name { font-size: 22px; }
  .card--back .brand-tile { left: 282px; top: 77px; width: 340px; height: 366px; }
  .card--back .brand-tile__name { font-size: 25px; }

  .accent-bar {
    position: absolute; left: 653px; right: 0; top: 421px; height: 43px;
    background: var(--brick-red);
  }
  .grid-lines { position: absolute; inset: 0; width: 100%; height: 100%; }
  .grid-lines path { fill: none; stroke: var(--grid-line); stroke-width: 2; }
</style>
</head>
<body>

<section class="card card--front" aria-label="Business card front">
  <h1 class="holder-name">DORRAN VELSBY</h1>
  <p class="holder-role">Owner</p>

  <div class="contact-rail"><div class="contact-rail__cap"></div></div>

  <ul class="contact-list">
    <li class="contact-item contact-item--phone">
      <span class="contact-item__icon"><svg viewBox="0 0 24 24"><path d="M7 2h10a1.5 1.5 0 0 1 1.5 1.5v17A1.5 1.5 0 0 1 17 22H7a1.5 1.5 0 0 1-1.5-1.5v-17A1.5 1.5 0 0 1 7 2zm0.5 2v14h9V4zm4.5 15a1 1 0 1 0 0 2 1 1 0 0 0 0-2z"/></svg></span>
      <span class="contact-item__text">928-555-0147</span>
    </li>
    <li class="contact-item contact-item--mail">
      <span class="contact-item__icon"><svg viewBox="0 0 24 24"><path d="M3 5h18a1 1 0 0 1 1 1v12a1 1 0 0 1-1 1H3a1 1 0 0 1-1-1V6a1 1 0 0 1 1-1zm1 2.3V17h16V7.3l-8 5.2z"/><path d="M4 6.5h16L12 11.7z"/></svg></span>
      <span class="contact-item__text">info@quarlwick.com</span>
    </li>
    <li class="contact-item contact-item--web">
      <span class="contact-item__icon"><svg viewBox="0 0 24 24"><path d="M12 2a10 10 0 1 0 0 20 10 10 0 0 0 0-20zm0 2c1.2 1.4 2 3.6 2.2 7H9.8C10 7.6 10.8 5.4 12 4zm-2.6.5C8.5 6.2 7.9 8.4 7.8 11H4.1a8 8 0 0 1 5.3-6.5zm5.2 0A8 8 0 0 1 19.9 11h-3.7c-.1-2.6-.7-4.8-1.6-6.5zM4.1 13h3.7c.1 2.6.7 4.8 1.6 6.5A8 8 0 0 1 4.1 13zm5.7 0h4.4c-.2 3.4-1 5.6-2.2 7-1.2-1.4-2-3.6-2.2-7zm6.4 0h3.7a8 8 0 0 1-5.3 6.5c.9-1.7 1.5-3.9 1.6-6.5z"/></svg></span>
      <span class="contact-item__text">www.quarlwick.com</span>
    </li>
    <li class="contact-item contact-item--place">
      <span class="contact-item__icon"><svg viewBox="0 0 24 24"><path d="M12 2a7 7 0 0 0-7 7c0 5.2 7 13 7 13s7-7.8 7-13a7 7 0 0 0-7-7zm0 9.5A2.5 2.5 0 1 1 12 6.5a2.5 2.5 0 0 1 0 5z"/></svg></span>
      <span class="contact-item__text">210 Street, Kestrel Bay City, AZ 12345</span>
    </li>
  </ul>

  <div class="brand-tile" role="img" aria-label="Company logo area: textured concrete tile with brick wall, city buildings and mason tools">
    <p class="brand-tile__name">QUARLWICK BUILDERS</p>
  </div>

  <div class="accent-bar"></div>
</section>

<section class="card card--back" aria-label="Business card back">
  <svg class="grid-lines" viewBox="0 0 904 518" aria-hidden="true">
    <path d="M0 65 H176 V0"/>
    <path d="M76 0 V127 H0"/>
    <path d="M0 140 H190 V518"/>
    <path d="M0 353 H160 V518"/>
    <path d="M0 430 H120"/>
    <path d="M540 0 V67 H904"/>
    <path d="M795 67 V375 H904"/>
    <path d="M680 128 H904"/>
    <path d="M680 128 V300 H904"/>
    <path d="M590 300 V518"/>
    <path d="M420 470 H904"/>
  </svg>
  <div class="brand-tile" role="img" aria-label="Company logo area: textured concrete tile with brick wall, city buildings and mason tools">
    <p class="brand-tile__name">QUARLWICK BUILDERS</p>
  </div>
</section>

</body>
</html>
```